Innovative Freezer Label Design

Create a versatile and innovative freezer label design with universal appeal, suitable for different functionalities. The design should cater to a diverse audience, including those who freeze meals for meal prepping, batch cooking, and the restaurant industry. Our vision is a visually striking and distinctive design that embodies simplicity.

Example "our current labels feature essential details like "Contents" and "Date." We recognize these as crucial points of information. Currently, the challenge lies in creating various labels for different marketplaces, considering language barriers. A proposed solution involves the integration of universal icons to replace specific words, promoting practicality for international sales."

Kindly note that design concepts should not be restricted to our current product, brand guideline, logo, or the provided example.

Our goal is not only product differentiation but also increased sales through a blend of functionality and aesthetics.

The following are examples of freezer labels designs. Kindly do not restrict your designs to the examples. The designs must be universal (for language barrier purposes)

Examples:
https://www.snaprovel.co.uk/pin/5820174630298837415/
https://www.snaprovel.co.uk/pin/5820174630298837419/
https://www.snaprovel.co.uk/pin/5820174630298837408/
https://www.snaprovel.co.uk/pin/5820174630298837322/
https://www.snaprovel.co.uk/pin/5820174630298898764/

Please reach out if you have any questions.

Thank you

```html
<!DOCTYPE html>
<html lang="en">
<head>
<meta charset="utf-8">
<title>Freezer Label Sheet</title>
<link href="https://fonts.googleapis.com/css2?family=Open+Sans:wght@400;600;700&display=swap" rel="stylesheet">
<style>
  :root {
    --canvas: #ffffff;
    --sheet: #ebebef;
    --label: #ffffff;
    --label-border: #c3cad3;
    --tab-dark: #1e5670;
    --tab-light: #e3e8ee;
    --icon-light: #ffffff;
    --icon-dark: #1e5670;
    --rule: #a9b0b8;
    --brand: #1e5670;
  }
  html, body {
    margin: 0;
    padding: 0;
    width: 1200px;
    height: 626px;
    overflow: hidden;
    background: var(--canvas);
    font-family: "Open Sans", sans-serif;
  }
  .icon-defs { position: absolute; width: 0; height: 0; }
  .sheet {
    position: absolute;
    left: 380px;
    top: 18px;
    width: 440px;
    height: 590px;
    box-sizing: border-box;
    padding: 13px 12px 13px 14px;
    background: var(--sheet);
    display: grid;
    grid-template-columns: repeat(2, 201px);
    grid-template-rows: repeat(5, 108px);
    column-gap: 13px;
    row-gap: 6px;
  }
  .label {
    position: relative;
    background: var(--label);
    border: 1px solid var(--label-border);
    border-radius: 6px;
    overflow: hidden;
    display: flex;
  }
  .label__tab {
    width: 22px;
    flex: none;
    display: flex;
    flex-direction: column;
    align-items: center;
    background: var(--tab-light);
  }
  .label__contents {
    width: 100%;
    height: 65px;
    background: var(--tab-dark);
    display: flex;
    align-items: center;
    justify-content: center;
  }
  .icon { display: block; fill: none; stroke-linecap: round; stroke-linejoin: round; }
  .icon--contents { width: 14px; height: 14px; stroke: var(--icon-light); stroke-width: 1.6; }
  .icon--date { width: 11px; height: 11px; margin-top: 5px; stroke: var(--icon-dark); stroke-width: 1.6; }
  .label__body { position: relative; flex: 1; }
  .label__rule {
    position: absolute;
    left: 3px;
    right: 8px;
    border-top: 1px dotted var(--rule);
  }
  .label__rule--1 { top: 22px; }
  .label__rule--2 { top: 40px; }
  .label__rule--3 { top: 57px; }
  .label__rule--4 { top: 77px; }
  .label__brand {
    position: absolute;
    left: 3px;
    top: 82px;
    font-size: 9px;
    font-weight: 700;
    color: var(--brand);
    letter-spacing: 0.4px;
  }
</style>
</head>
<body>
  <svg class="icon-defs" aria-hidden="true">
    <symbol id="icon-contents" viewBox="0 0 24 24">
      <path d="M6 3v6a2 2 0 0 0 4 0V3M8 3v18"/>
      <path d="M17 21V3c-2.2 1.5-3 4-3 7v3h3"/>
    </symbol>
    <symbol id="icon-date" viewBox="0 0 24 24">
      <rect x="3" y="5" width="18" height="16" rx="2"/>
      <path d="M3 10h18M8 3v4M16 3v4"/>
    </symbol>
  </svg>
  <main class="sheet">
    <div class="label"><div class="label__tab"><div class="label__contents"><svg class="icon icon--contents" role="img" aria-label="Contents"><use href="#icon-contents"/></svg></div><svg class="icon icon--date" role="img" aria-label="Date"><use href="#icon-date"/></svg></div><div class="label__body"><div class="label__rule label__rule--1"></div><div class="label__rule label__rule--2"></div><div class="label__rule label__rule--3"></div><div class="label__rule label__rule--4"></div><div class="label__brand">Novaleaf</div></div></div>
    <div class="label"><div class="label__tab"><div class="label__contents"><svg class="icon icon--contents" role="img" aria-label="Contents"><use href="#icon-contents"/></svg></div><svg class="icon icon--date" role="img" aria-label="Date"><use href="#icon-date"/></svg></div><div class="label__body"><div class="label__rule label__rule--1"></div><div class="label__rule label__rule--2"></div><div class="label__rule label__rule--3"></div><div class="label__rule label__rule--4"></div><div class="label__brand">Novaleaf</div></div></div>
    <div class="label"><div class="label__tab"><div class="label__contents"><svg class="icon icon--contents" role="img" aria-label="Contents"><use href="#icon-contents"/></svg></div><svg class="icon icon--date" role="img" aria-label="Date"><use href="#icon-date"/></svg></div><div class="label__body"><div class="label__rule label__rule--1"></div><div class="label__rule label__rule--2"></div><div class="label__rule label__rule--3"></div><div class="label__rule label__rule--4"></div><div class="label__brand">Novaleaf</div></div></div>
    <div class="label"><div class="label__tab"><div class="label__contents"><svg class="icon icon--contents" role="img" aria-label="Contents"><use href="#icon-contents"/></svg></div><svg class="icon icon--date" role="img" aria-label="Date"><use href="#icon-date"/></svg></div><div class="label__body"><div class="label__rule label__rule--1"></div><div class="label__rule label__rule--2"></div><div class="label__rule label__rule--3"></div><div class="label__rule label__rule--4"></div><div class="label__brand">Novaleaf</div></div></div>
    <div class="label"><div class="label__tab"><div class="label__contents"><svg class="icon icon--contents" role="img" aria-label="Contents"><use href="#icon-contents"/></svg></div><svg class="icon icon--date" role="img" aria-label="Date"><use href="#icon-date"/></svg></div><div class="label__body"><div class="label__rule label__rule--1"></div><div class="label__rule label__rule--2"></div><div class="label__rule label__rule--3"></div><div class="label__rule label__rule--4"></div><div class="label__brand">Novaleaf</div></div></div>
    <div class="label"><div class="label__tab"><div class="label__contents"><svg class="icon icon--contents" role="img" aria-label="Contents"><use href="#icon-contents"/></svg></div><svg class="icon icon--date" role="img" aria-label="Date"><use href="#icon-date"/></svg></div><div class="label__body"><div class="label__rule label__rule--1"></div><div class="label__rule label__rule--2"></div><div class="label__rule label__rule--3"></div><div class="label__rule label__rule--4"></div><div class="label__brand">Novaleaf</div></div></div>
    <div class="label"><div class="label__tab"><div class="label__contents"><svg class="icon icon--contents" role="img" aria-label="Contents"><use href="#icon-contents"/></svg></div><svg class="icon icon--date" role="img" aria-label="Date"><use href="#icon-date"/></svg></div><div class="label__body"><div class="label__rule label__rule--1"></div><div class="label__rule label__rule--2"></div><div class="label__rule label__rule--3"></div><div class="label__rule label__rule--4"></div><div class="label__brand">Novaleaf</div></div></div>
    <div class="label"><div class="label__tab"><div class="label__contents"><svg class="icon icon--contents" role="img" aria-label="Contents"><use href="#icon-contents"/></svg></div><svg class="icon icon--date" role="img" aria-label="Date"><use href="#icon-date"/></svg></div><div class="label__body"><div class="label__rule label__rule--1"></div><div class="label__rule label__rule--2"></div><div class="label__rule label__rule--3"></div><div class="label__rule label__rule--4"></div><div class="label__brand">Novaleaf</div></div></div>
    <div class="label"><div class="label__tab"><div class="label__contents"><svg class="icon icon--contents" role="img" aria-label="Contents"><use href="#icon-contents"/></svg></div><svg class="icon icon--date" role="img" aria-label="Date"><use href="#icon-date"/></svg></div><div class="label__body"><div class="label__rule label__rule--1"></div><div class="label__rule label__rule--2"></div><div class="label__rule label__rule--3"></div><div class="label__rule label__rule--4"></div><div class="label__brand">Novaleaf</div></div></div>
    <div class="label"><div class="label__tab"><div class="label__contents"><svg class="icon icon--contents" role="img" aria-label="Contents"><use href="#icon-contents"/></svg></div><svg class="icon icon--date" role="img" aria-label="Date"><use href="#icon-date"/></svg></div><div class="label__body"><div class="label__rule label__rule--1"></div><div class="label__rule label__rule--2"></div><div class="label__rule label__rule--3"></div><div class="label__rule label__rule--4"></div><div class="label__brand">Novaleaf</div></div></div>
  </main>
</body>
</html>
```